Etiquetas para platos preparados de la marca Tarvelia

Necesito el diseño de una belly band o etiquetas para productos cocinados. En ella debe aparecer la siguiente información: el logo de la marca,
Símbolos con la siguiente info: refrigerado entre 2º-4º, pincha el plástico que lo cubre, imagen microondas 3:00, disfruta.
Además necesito que la etiqueta tenga en la parte frontal una zona donde podamos modificar e ir añadiendo el nombre del producto en concreto y en la parte trasera una zona destinada también a los valores nutricionales personalizable.
Por último necesitamos que las etiquetas estén diseñadas en 6 colores diferentes para poder diferenciar entre diferentes categorías (ensaladas, carnes, pescados, postres, ECO...).
Los tamaños de los envases sobre los que debe ir el belly band es el siguiente:
-Formato 1: 180x180x35mm
-Formato 2: 168x128x35mm
-Formato 3: belly band de 30cm de largo

Otro

Target Market(s)

Producto expuesto es vitrinas expositoras de supermercados

Industry/Entity Type

Alimentación

Font styles to use
Sans Serif
Other font styles liked:
• Cocomat y Poppins

Requirements
Must have
• Atractivo visualmente. Fuentes empleadas Cocomat y Montserrat
Nice to have
• Los colores para diferenciar categorías y espacio para poder incluir nosotros el nombre de cada producto. Además un espacio que ponga Origen personalizable también y un logo que ponga casero 100%

```html
<!DOCTYPE html>
<html lang="es">
<head>
<meta charset="utf-8">
<title>Tarvelia · Belly bands 300x60</title>
<link href="https://fonts.googleapis.com/css2?family=Poppins:wght@200;300&family=Montserrat:wght@400;500&display=swap" rel="stylesheet">
<style>
  :root{
    --kraft:#946b55;
    --ink:#000000;
    --guide-blue:#4a5bd0;
    --guide-red:#e0403a;
    --guide-green:#3fbf4a;
    --pescados:#72f0c4;
    --carnes:#b44c98;
    --ensaladas:#55ff55;
    --entrantes:#ff8c55;
    --fritos:#e8ac10;
    --postres:#d6c4fc;
    --paper:#ffffff;
  }
  *{margin:0;padding:0;box-sizing:border-box}
  html,body{width:900px;height:1200px;overflow:hidden;background:var(--paper)}
  .sheet{position:relative;width:900px;height:1200px;font-family:"Montserrat",sans-serif;color:var(--ink)}
  .fold{position:absolute;top:26px;height:1025px;border-left:1px dashed #333;z-index:2}
  .fold--a{left:352px}
  .fold--b{left:547px}
  .band{position:absolute;left:122px;width:655px;height:129px;background:var(--kraft);border:1px solid var(--guide-blue);overflow:hidden}
  .band::before,.band::after{content:"";position:absolute;pointer-events:none}
  .band::before{inset:4px 5px 5px 5px;border:1px solid var(--guide-red)}
  .band::after{inset:8px 9px 9px 9px;border:1px solid var(--guide-green);opacity:.8}
  .band__category{position:absolute;left:325px;top:0;width:100px;height:100%;background:var(--cat)}
  .rule{position:absolute;height:0;border-top:1px solid var(--ink);opacity:.75}
  .copy{position:absolute;writing-mode:vertical-rl;font-size:6.2px;line-height:7.4px;height:92px;width:54px;overflow:hidden;color:var(--ink)}
  .copy--back{transform:rotate(180deg)}
  .brand-vertical{position:absolute;left:110px;top:20px;writing-mode:vertical-rl;font-family:"Poppins",sans-serif;font-weight:300;font-size:20px;letter-spacing:1px;color:var(--ink)}
  .title{position:absolute;left:236px;top:6px;font-family:"Poppins",sans-serif;font-weight:300;font-size:31px;line-height:1.2;letter-spacing:.5px;white-space:nowrap;color:var(--ink);z-index:1}
  .snow{position:absolute;left:253px;top:62px;font-size:16px;line-height:1}
  .note{position:absolute;font-size:4px;line-height:4.6px;text-align:center}
  .note--fridge{left:244px;top:82px;width:34px}
  .note--heat{left:236px;top:112px;width:50px}
  .microwave{position:absolute;left:250px;top:95px;width:18px;height:14px}
  .art{position:absolute;background:var(--artfill,rgba(0,0,0,.3));border-radius:6px}
  .art--front{left:345px;top:40px;width:80px;height:58px;--artfill:rgba(0,0,0,.25)}
  .art--back{left:517px;top:40px;width:38px;height:50px;--artfill:rgba(0,0,0,.4)}
  .seal{position:absolute;top:104px;width:14px;height:14px;border-radius:50%;border:2px solid var(--ink)}
  .seal--one{left:338px}
  .seal--two{left:356px}
  .brand{position:absolute;left:378px;top:107px;font-size:8px;font-weight:500}
  .size{position:absolute;left:0;width:900px;top:1092px;text-align:center;font-family:"Poppins",sans-serif;font-weight:300;font-size:54px;line-height:1;color:var(--ink)}
</style>
</head>
<body>
<div class="sheet">
  <div class="fold fold--a"></div>
  <div class="fold fold--b"></div>

  <section class="band" style="top:52px;--cat:var(--pescados)">
    <div class="band__category"></div>
    <div class="rule" style="left:20px;top:14px;width:90px"></div><div class="rule" style="left:143px;top:14px;width:70px"></div>
    <div class="rule" style="left:20px;top:115px;width:90px"></div><div class="rule" style="left:143px;top:115px;width:70px"></div>
    <p class="copy" style="left:24px;top:20px">Lorem ipsum dolor sit amet, consectetuer adipiscing elit, sed diam nonummy nibh euismod tincidunt ut laoreet dolore magna aliquam erat volutpat. Ut wisi enim ad minim Lorem ipsum</p>
    <p class="brand-vertical">TARVELIA</p>
    <p class="copy" style="left:148px;top:20px">Lorem ipsum dolor sit amet, consectetuer adipiscing elit, sed diam nonummy nibh euismod tincidunt ut laoreet dolore magna aliquam erat volutpat. Ut wisi enim ad minim Lorem ipsum</p>
    <div class="art art--front" role="img" aria-label="Ilustración a tinta de un pescado"></div>
    <h2 class="title">PESCADOS</h2>
    <span class="snow">✻</span>
    <p class="note note--fridge">8 minutos en el frigorífico</p>
    <svg class="microwave" viewBox="0 0 18 14"><rect x="1" y="1" width="16" height="12" fill="none" stroke="#000" stroke-width="1.2"/><rect x="3" y="3" width="9" height="8" fill="none" stroke="#000"/><line x1="14.5" y1="3.5" x2="14.5" y2="10.5" stroke="#000"/></svg>
    <p class="note note--heat">calentar 3 minutos</p>
    <span class="seal seal--one"></span><span class="seal seal--two"></span>
    <span class="brand">Tarvelia</span>
    <div class="rule" style="left:434px;top:14px;width:200px"></div><div class="rule" style="left:434px;top:115px;width:200px"></div>
    <p class="copy copy--back" style="left:444px;top:20px">Lorem ipsum dolor sit amet, consectetuer adipiscing elit, sed diam nonummy nibh euismod tincidunt ut laoreet dolore magna aliquam erat volutpat. Ut wisi enim ad minim Lorem ipsum</p>
    <div class="art art--back" role="img" aria-label="Pequeña ilustración de un pescado"></div>
    <p class="copy copy--back" style="left:572px;top:20px">Lorem ipsum dolor sit amet, consectetuer adipiscing elit, sed diam nonummy nibh euismod tincidunt ut laoreet dolore magna aliquam erat volutpat. Ut wisi enim ad minim Lorem ipsum</p>
  </section>

  <section class="band" style="top:219px;--cat:var(--carnes)">
    <div class="band__category"></div>
    <div class="rule" style="left:20px;top:14px;width:90px"></div><div class="rule" style="left:143px;top:14px;width:70px"></div>
    <div class="rule" style="left:20px;top:115px;width:90px"></div><div class="rule" style="left:143px;top:115px;width:70px"></div>
    <p class="copy" style="left:24px;top:20px">Lorem ipsum dolor sit amet, consectetuer adipiscing elit, sed diam nonummy nibh euismod tincidunt ut laoreet dolore magna aliquam erat volutpat. Ut wisi enim ad minim Lorem ipsum</p>
    <p class="brand-vertical">TARVELIA</p>
    <p class="copy" style="left:148px;top:20px">Lorem ipsum dolor sit amet, consectetuer adipiscing elit, sed diam nonummy nibh euismod tincidunt ut laoreet dolore magna aliquam erat volutpat. Ut wisi enim ad minim Lorem ipsum</p>
    <div class="art art--front" role="img" aria-label="Ilustración a tinta de un filete de carne"></div>
    <h2 class="title">CARNES</h2>
    <span class="snow">✻</span>
    <p class="note note--fridge">8 minutos en el frigorífico</p>
    <svg class="microwave" viewBox="0 0 18 14"><rect x="1" y="1" width="16" height="12" fill="none" stroke="#000" stroke-width="1.2"/><rect x="3" y="3" width="9" height="8" fill="none" stroke="#000"/><line x1="14.5" y1="3.5" x2="14.5" y2="10.5" stroke="#000"/></svg>
    <p class="note note--heat">calentar 3 minutos</p>
    <span class="seal seal--one"></span><span class="seal seal--two"></span>
    <span class="brand">Tarvelia</span>
    <div class="rule" style="left:434px;top:14px;width:200px"></div><div class="rule" style="left:434px;top:115px;width:200px"></div>
    <p class="copy copy--back" style="left:444px;top:20px">Lorem ipsum dolor sit amet, consectetuer adipiscing elit, sed diam nonummy nibh euismod tincidunt ut laoreet dolore magna aliquam erat volutpat. Ut wisi enim ad minim Lorem ipsum</p>
    <div class="art art--back" role="img" aria-label="Pequeña ilustración de un filete"></div>
    <p class="copy copy--back" style="left:572px;top:20px">Lorem ipsum dolor sit amet, consectetuer adipiscing elit, sed diam nonummy nibh euismod tincidunt ut laoreet dolore magna aliquam erat volutpat. Ut wisi enim ad minim Lorem ipsum</p>
  </section>

  <section class="band" style="top:395px;--cat:var(--ensaladas)">
    <div class="band__category"></div>
    <div class="rule" style="left:20px;top:14px;width:90px"></div><div class="rule" style="left:143px;top:14px;width:70px"></div>
    <div class="rule" style="left:20px;top:115px;width:90px"></div><div class="rule" style="left:143px;top:115px;width:70px"></div>
    <p class="copy" style="left:24px;top:20px">Lorem ipsum dolor sit amet, consectetuer adipiscing elit, sed diam nonummy nibh euismod tincidunt ut laoreet dolore magna aliquam erat volutpat. Ut wisi enim ad minim Lorem ipsum</p>
    <p class="brand-vertical">TARVELIA</p>
    <p class="copy" style="left:148px;top:20px">Lorem ipsum dolor sit amet, consectetuer adipiscing elit, sed diam nonummy nibh euismod tincidunt ut laoreet dolore magna aliquam erat volutpat. Ut wisi enim ad minim Lorem ipsum</p>
    <div class="art art--front" role="img" aria-label="Ilustración a tinta de un bol de ensalada"></div>
    <h2 class="title">ENSALADAS</h2>
    <span class="snow">✻</span>
    <p class="note note--fridge">8 minutos en el frigorífico</p>
    <svg class="microwave" viewBox="0 0 18 14"><rect x="1" y="1" width="16" height="12" fill="none" stroke="#000" stroke-width="1.2"/><rect x="3" y="3" width="9" height="8" fill="none" stroke="#000"/><line x1="14.5" y1="3.5" x2="14.5" y2="10.5" stroke="#000"/></svg>
    <p class="note note--heat">calentar 3 minutos</p>
    <span class="seal seal--one"></span><span class="seal seal--two"></span>
    <span class="brand">Tarvelia</span>
    <div class="rule" style="left:434px;top:14px;width:200px"></div><div class="rule" style="left:434px;top:115px;width:200px"></div>
    <p class="copy copy--back" style="left:444px;top:20px">Lorem ipsum dolor sit amet, consectetuer adipiscing elit, sed diam nonummy nibh euismod tincidunt ut laoreet dolore magna aliquam erat volutpat. Ut wisi enim ad minim Lorem ipsum</p>
    <div class="art art--back" role="img" aria-label="Pequeña ilustración de un bol de ensalada"></div>
    <p class="copy copy--back" style="left:572px;top:20px">Lorem ipsum dolor sit amet, consectetuer adipiscing elit, sed diam nonummy nibh euismod tincidunt ut laoreet dolore magna aliquam erat volutpat. Ut wisi enim ad minim Lorem ipsum</p>
  </section>

  <section class="band" style="top:567px;--cat:var(--entrantes)">
    <div class="band__category"></div>
    <div class="rule" style="left:20px;top:14px;width:90px"></div><div class="rule" style="left:143px;top:14px;width:70px"></div>
    <div class="rule" style="left:20px;top:115px;width:90px"></div><div class="rule" style="left:143px;top:115px;width:70px"></div>
    <p class="copy" style="left:24px;top:20px">Lorem ipsum dolor sit amet, consectetuer adipiscing elit, sed diam nonummy nibh euismod tincidunt ut laoreet dolore magna aliquam erat volutpat. Ut wisi enim ad minim Lorem ipsum</p>
    <p class="brand-vertical">TARVELIA</p>
    <p class="copy" style="left:148px;top:20px">Lorem ipsum dolor sit amet, consectetuer adipiscing elit, sed diam nonummy nibh euismod tincidunt ut laoreet dolore magna aliquam erat volutpat. Ut wisi enim ad minim Lorem ipsum</p>
    <div class="art art--front" role="img" aria-label="Ilustración a tinta de canapés y pinchos"></div>
    <h2 class="title">ENTRANTES</h2>
    <span class="snow">✻</span>
    <p class="note note--fridge">8 minutos en el frigorífico</p>
    <svg class="microwave" viewBox="0 0 18 14"><rect x="1" y="1" width="16" height="12" fill="none" stroke="#000" stroke-width="1.2"/><rect x="3" y="3" width="9" height="8" fill="none" stroke="#000"/><line x1="14.5" y1="3.5" x2="14.5" y2="10.5" stroke="#000"/></svg>
    <p class="note note--heat">calentar 3 minutos</p>
    <span class="seal seal--one"></span><span class="seal seal--two"></span>
    <span class="brand">Tarvelia</span>
    <div class="rule" style="left:434px;top:14px;width:200px"></div><div class="rule" style="left:434px;top:115px;width:200px"></div>
    <p class="copy copy--back" style="left:444px;top:20px">Lorem ipsum dolor sit amet, consectetuer adipiscing elit, sed diam nonummy nibh euismod tincidunt ut laoreet dolore magna aliquam erat volutpat. Ut wisi enim ad minim Lorem ipsum</p>
    <div class="art art--back" role="img" aria-label="Pequeña ilustración de canapés"></div>
    <p class="copy copy--back" style="left:572px;top:20px">Lorem ipsum dolor sit amet, consectetuer adipiscing elit, sed diam nonummy nibh euismod tincidunt ut laoreet dolore magna aliquam erat volutpat. Ut wisi enim ad minim Lorem ipsum</p>
  </section>

  <section class="band" style="top:740px;--cat:var(--fritos)">
    <div class="band__category"></div>
    <div class="rule" style="left:20px;top:14px;width:90px"></div><div class="rule" style="left:143px;top:14px;width:70px"></div>
    <div class="rule" style="left:20px;top:115px;width:90px"></div><div class="rule" style="left:143px;top:115px;width:70px"></div>
    <p class="copy" style="left:24px;top:20px">Lorem ipsum dolor sit amet, consectetuer adipiscing elit, sed diam nonummy nibh euismod tincidunt ut laoreet dolore magna aliquam erat volutpat. Ut wisi enim ad minim Lorem ipsum</p>
    <p class="brand-vertical">TARVELIA</p>
    <p class="copy" style="left:148px;top:20px">Lorem ipsum dolor sit amet, consectetuer adipiscing elit, sed diam nonummy nibh euismod tincidunt ut laoreet dolore magna aliquam erat volutpat. Ut wisi enim ad minim Lorem ipsum</p>
    <div class="art art--front" role="img" aria-label="Ilustración a tinta de patatas fritas"></div>
    <h2 class="title">FRITOS</h2>
    <span class="snow">✻</span>
    <p class="note note--fridge">8 minutos en el frigorífico</p>
    <svg class="microwave" viewBox="0 0 18 14"><rect x="1" y="1" width="16" height="12" fill="none" stroke="#000" stroke-width="1.2"/><rect x="3" y="3" width="9" height="8" fill="none" stroke="#000"/><line x1="14.5" y1="3.5" x2="14.5" y2="10.5" stroke="#000"/></svg>
    <p class="note note--heat">calentar 3 minutos</p>
    <span class="seal seal--one"></span><span class="seal seal--two"></span>
    <span class="brand">Tarvelia</span>
    <div class="rule" style="left:434px;top:14px;width:200px"></div><div class="rule" style="left:434px;top:115px;width:200px"></div>
    <p class="copy copy--back" style="left:444px;top:20px">Lorem ipsum dolor sit amet, consectetuer adipiscing elit, sed diam nonummy nibh euismod tincidunt ut laoreet dolore magna aliquam erat volutpat. Ut wisi enim ad minim Lorem ipsum</p>
    <div class="art art--back" role="img" aria-label="Pequeña ilustración de patatas fritas"></div>
    <p class="copy copy--back" style="left:572px;top:20px">Lorem ipsum dolor sit amet, consectetuer adipiscing elit, sed diam nonummy nibh euismod tincidunt ut laoreet dolore magna aliquam erat volutpat. Ut wisi enim ad minim Lorem ipsum</p>
  </section>

  <section class="band" style="top:916px;--cat:var(--postres)">
    <div class="band__category"></div>
    <div class="rule" style="left:20px;top:14px;width:90px"></div><div class="rule" style="left:143px;top:14px;width:70px"></div>
    <div class="rule" style="left:20px;top:115px;width:90px"></div><div class="rule" style="left:143px;top:115px;width:70px"></div>
    <p class="copy" style="left:24px;top:20px">Lorem ipsum dolor sit amet, consectetuer adipiscing elit, sed diam nonummy nibh euismod tincidunt ut laoreet dolore magna aliquam erat volutpat. Ut wisi enim ad minim Lorem ipsum</p>
    <p class="brand-vertical">TARVELIA</p>
    <p class="copy" style="left:148px;top:20px">Lorem ipsum dolor sit amet, consectetuer adipiscing elit, sed diam nonummy nibh euismod tincidunt ut laoreet dolore magna aliquam erat volutpat. Ut wisi enim ad minim Lorem ipsum</p>
    <div class="art art--front" role="img" aria-label="Ilustración a tinta de tortitas con frutos rojos"></div>
    <h2 class="title">POSTRES</h2>
    <span class="snow">✻</span>
    <p class="note note--fridge">8 minutos en el frigorífico</p>
    <svg class="microwave" viewBox="0 0 18 14"><rect x="1" y="1" width="16" height="12" fill="none" stroke="#000" stroke-width="1.2"/><rect x="3" y="3" width="9" height="8" fill="none" stroke="#000"/><line x1="14.5" y1="3.5" x2="14.5" y2="10.5" stroke="#000"/></svg>
    <p class="note note--heat">calentar 3 minutos</p>
    <span class="seal seal--one"></span><span class="seal seal--two"></span>
    <span class="brand">Tarvelia</span>
    <div class="rule" style="left:434px;top:14px;width:200px"></div><div class="rule" style="left:434px;top:115px;width:200px"></div>
    <p class="copy copy--back" style="left:444px;top:20px">Lorem ipsum dolor sit amet, consectetuer adipiscing elit, sed diam nonummy nibh euismod tincidunt ut laoreet dolore magna aliquam erat volutpat. Ut wisi enim ad minim Lorem ipsum</p>
    <div class="art art--back" role="img" aria-label="Pequeña ilustración de tortitas"></div>
    <p class="copy copy--back" style="left:572px;top:20px">Lorem ipsum dolor sit amet, consectetuer adipiscing elit, sed diam nonummy nibh euismod tincidunt ut laoreet dolore magna aliquam erat volutpat. Ut wisi enim ad minim Lorem ipsum</p>
  </section>

  <p class="size">300x60</p>
</div>
</body>
</html>
```